Business Card Design, including supply of raw art files plus a vector diagram of the flenzo logo and

We need the business card design for a company that is launching a new exciting product. The brief requires the submission of the following once the final design is chosen:

- business card layout including raw files
- a composite vector image file of the flenzo logo and tag line
- a standalone vector image file of the flenzo logo

The product will be launched as a customer engagement app.

It has 4 core modules which enables a person to do multiple things - book tours and activities, order takeaways, search for local deals and offers. A universal currency is at the heart of this product. When you use the app, you earn cashback rewards when shopping or buying at any of the merchant partners across the modules as . These rewards can then be used as full or part payment when buying goods or services at these merchant partners.

The business card must help us build the brand, communicate the benefit of the brand's key focus - the ability to earn and burn this universal cashback ccurrency - across the 4 modules - booking of tours and activities, ordering, searching for local deals and payment.

We would like the design to use the brand's blue colour the hex colour is: 00
Dark grey : 646464
Darker blue shadow: 058bdd
Main Blue: 0084ff

We need to translate this into a CMYK print or spot colour print.

Both print options to be supplied as separate files.

An example of the base concept we have in mind is attached for your reference.

The font used by the brand is Proxima Nova.

Industry/Entity Type

Business

Contact Information for Business Card

Carla Whitfield
Marketing
W: www.flenzo.co
M: + 61 407318265
T: +61 2 9375 4120
A: Suite 7, Level 2, 14-18 Harrow Lane, Sydney, NSW, 2000, Australia

Font styles to use
Sans Serif

Requirements
Must have
• flEnzo logo and tagline
• address details
• flEnzo icons as supplied
Nice to have
• would like to have the option of a spot varnish layer over the logo and icons at the back of the card

```html
<!DOCTYPE html>
<html lang="en">
<head>
<meta charset="utf-8">
<title>flEnzo business card</title>
<link rel="stylesheet" href="https://fonts.googleapis.com/css2?family=Montserrat:wght@200;400;500&display=swap">
<style>
  :root {
    --main-blue: #0084ff;
    --deep-blue: #058bdd;
    --dark-grey: #646464;
    --charcoal: #3f4247;
    --ink: #4a4a4a;
    --card-white: #fbfbfb;
    --card-black: #1d1e20;
    --backdrop: #e9e9ea;
  }
  * { box-sizing: border-box; margin: 0; padding: 0; }
  html, body {
    width: 1200px; height: 716px; overflow: hidden;
    background: var(--backdrop);
    font-family: "Montserrat", sans-serif;
  }
  .stage {
    position: relative; width: 1200px; height: 716px;
    display: flex; align-items: center; justify-content: center; gap: 40px;
  }
  .card {
    position: relative; width: 540px; height: 330px; overflow: hidden;
    box-shadow: 0 6px 18px rgba(0,0,0,.18);
  }
  .card-back {
    background: var(--card-black);
    display: flex; align-items: center; justify-content: center;
  }
  .back-mark {
    width: 118px; height: 118px; border-radius: 50%;
    background: radial-gradient(circle at 35% 30%, #3aa6ff, var(--deep-blue) 70%);
  }
  .card-front { background: var(--card-white); }
  .wave { position: absolute; inset: 0; width: 540px; height: 330px; }
  .brand {
    position: absolute; left: 34px; top: 58px;
    display: flex; align-items: center; gap: 14px;
  }
  .brand-dot {
    width: 52px; height: 52px; border-radius: 50%; background: var(--deep-blue);
  }
  .brand-name {
    font-weight: 200; font-size: 50px; color: var(--ink); letter-spacing: 1px;
  }
  .contact {
    position: absolute; left: 34px; top: 150px;
    list-style: none; font-size: 12px; line-height: 17px; color: var(--ink);
  }
  .contact li { display: flex; align-items: flex-start; gap: 8px; }
  .contact svg { width: 10px; height: 10px; margin-top: 3px; flex: none; }
  .contact .address { padding-left: 18px; }
  .person {
    position: absolute; right: 30px; top: 132px; text-align: right; color: #fff;
  }
  .person-name { font-weight: 500; font-size: 16px; }
  .person-role { font-weight: 400; font-size: 12px; margin-top: 4px; }
</style>
</head>
<body>
<main class="stage">
  <section class="card card-back" aria-label="Card back">
    <div class="back-mark"></div>
  </section>

  <section class="card card-front" aria-label="Card front">
    <svg class="wave" viewBox="0 0 540 330" aria-hidden="true">
      <path d="M120,0 C250,20 320,90 380,160 C430,215 480,250 540,262 L540,285 C470,270 420,235 370,180 C310,115 240,40 80,14 Z" fill="var(--charcoal)"/>
      <path d="M100,8 C240,28 310,100 370,168 C420,224 476,258 540,270" fill="none" stroke="var(--card-white)" stroke-width="4"/>
      <path d="M150,0 L540,0 L540,248 C478,236 430,196 385,145 C330,82 270,20 150,0 Z" fill="var(--main-blue)"/>
      <path d="M170,0 C280,20 340,80 395,140 C440,190 488,226 540,236 L540,0 Z" fill="var(--deep-blue)" opacity=".35"/>
    </svg>

    <div class="brand">
      <span class="brand-dot"></span>
      <span class="brand-name">flEnzo</span>
    </div>

    <ul class="contact">
      <li>
        <svg viewBox="0 0 10 10"><rect x="2.5" y="0.5" width="5" height="9" rx="1" fill="var(--main-blue)"/></svg>
        <span>+ 61 407318265</span>
      </li>
      <li>
        <svg viewBox="0 0 10 10"><path d="M1,3 C1,1 3,1 3,1 L4,3 L3,4 C4,6 5,7 6,7 L7,6 L9,7 C9,9 7,9 7,9 C4,9 1,6 1,3 Z" fill="var(--main-blue)"/></svg>
        <span>+61 2 9375 4120</span>
      </li>
      <li>
        <svg viewBox="0 0 10 10"><circle cx="5" cy="5" r="4.2" fill="none" stroke="var(--main-blue)" stroke-width="1.2"/><path d="M1,5 H9 M5,1 C3,3 3,7 5,9 M5,1 C7,3 7,7 5,9" fill="none" stroke="var(--main-blue)" stroke-width=".9"/></svg>
        <span>www.flenzo.co</span>
      </li>
      <li>
        <svg viewBox="0 0 10 10"><path d="M5,10 C2,6 1.5,4.5 1.5,3.5 A3.5,3.5 0 0 1 8.5,3.5 C8.5,4.5 8,6 5,10 Z" fill="var(--main-blue)"/><circle cx="5" cy="3.5" r="1.2" fill="var(--card-white)"/></svg>
        <span>Suite 7, Level 2, 14-18 Harrow Lane,</span>
      </li>
      <li class="address">Sydney, NSW, 2000, Australia</li>
    </ul>

    <div class="person">
      <p class="person-name">Carla Whitfield</p>
      <p class="person-role">Marketing</p>
    </div>
  </section>
</main>
</body>
</html>
```